Email Design Creative Design Needed

Our website is called CampusLedger.org. One of our competitor(varsity scout.us.com) is using the following email creative.
http://pqr.brightquill.com/Affiliate/Assets/3532.html
http://pqr.brightquill.com/Affiliate/Assets/7921.html
http://pqr.brightquill.com/Affiliate/Assets/8061.html

We would like to use similar email creative without copying their exact creative. You can use the above as a guide but then come up with your own version of the creative.
The above are just concepts, please be creative and come up with your own version of it, without feeling that they have been copied. Feel free to move the components around. Also, feel free to change the colours and text.

Please find attached the CampusLedger.org logo.

Reason: We would like to receive more designs.

College

```html
<!DOCTYPE html>
<html lang="en">
<head>
<meta charset="utf-8">
<title>CampusLedger.org – Degrees from Accredited Colleges</title>
<link rel="stylesheet" href="https://fonts.googleapis.com/css2?family=Open+Sans:wght@400;600;700&family=Roboto+Condensed:wght@700&display=swap">
<style>
  :root {
    --green: #a9c83b;
    --ink: #3c3c3c;
    --grey-text: #555;
    --tile-label: #7d7d7d;
    --button: #5b5b5b;
    --row-alt: #f3f3f3;
    --rule: #dcdcdc;
    --footer-bg: #ededed;
    --white: #ffffff;
  }
  * { box-sizing: border-box; margin: 0; padding: 0; }
  html, body { width: 776px; height: 1200px; overflow: hidden; background: var(--white); }
  body { font-family: "Open Sans", Arial, sans-serif; color: var(--ink); }

  .email { position: relative; width: 776px; height: 1200px; }

  /* Hero */
  .hero {
    position: absolute; left: 0; top: 0; width: 776px; height: 372px;
    background: linear-gradient(90deg, #f7f6f4 0%, #ecebe8 45%, #d9d3cc 100%);
    overflow: hidden;
  }
  .hero-photo {
    position: absolute; right: 0; top: 0; width: 420px; height: 372px;
    background: radial-gradient(ellipse at 55% 40%, #d8b49d 0%, #b58f7a 30%, #6f5a55 65%, #d2ccc6 100%);
  }
  .hero-swoosh { position: absolute; left: 0; top: 0; width: 776px; height: 372px; }
  .brand {
    position: absolute; left: 30px; top: 60px;
    font-family: "Open Sans", Arial, sans-serif; font-weight: 700;
    font-size: 26px; line-height: 1; color: var(--ink);
  }
  .hero-title {
    position: absolute; left: 76px; top: 142px; width: 260px;
    font-family: "Roboto Condensed", "Arial Narrow", sans-serif; font-weight: 700;
    font-size: 28px; line-height: 1.2; color: var(--ink); text-transform: uppercase;
  }

  /* Category tiles */
  .tiles {
    position: absolute; left: 34px; top: 392px; width: 712px; height: 140px;
    display: flex; gap: 10px;
  }
  .tile {
    flex: 1; border-radius: 10px; overflow: hidden; display: flex; flex-direction: column;
    box-shadow: 0 2px 5px rgba(0,0,0,.2);
  }
  .tile-photo { flex: 1; }
  .tile-photo.subject { background: linear-gradient(135deg, #6c86a8, #c9a77c); }
  .tile-photo.level { background: linear-gradient(135deg, #e7e3de, #2f2f35); }
  .tile-photo.state { background: linear-gradient(180deg, #7fa8d6, #7b5d4c 70%, #6d8a4b); }
  .tile-photo.online { background: linear-gradient(135deg, #bcd2e4, #7a90a6); }
  .tile-label {
    height: 40px; background: var(--tile-label); color: var(--white);
    font-size: 14px; font-weight: 600; text-transform: uppercase;
    display: flex; align-items: center; justify-content: center; text-align: center;
  }

  /* Salary table */
  .salary-table {
    position: absolute; left: 0; top: 588px; width: 776px;
    border-collapse: collapse; table-layout: fixed;
  }
  .salary-table col.occupation { width: 310px; }
  .salary-table col.salary { width: 234px; }
  .salary-table col.action { width: 232px; }
  .salary-table th {
    height: 48px; background: var(--green); color: var(--white);
    font-size: 19px; font-weight: 700; text-transform: uppercase; text-align: center;
    border-right: 2px solid var(--white);
  }
  .salary-table th:last-child { border-right: none; }
  .salary-table td {
    height: 86px; border-right: 1px solid var(--rule); border-bottom: 1px solid var(--rule);
    font-size: 17px; color: var(--grey-text);
  }
  .salary-table td:last-child { border-right: none; }
  .salary-table tbody tr:nth-child(even) td { background: var(--row-alt); }
  .occupation-cell { padding-left: 34px; line-height: 1.35; }
  .salary-cell { text-align: center; }
  .salary-cell strong { color: var(--ink); font-weight: 700; }
  .action-cell { text-align: center; }
  .cta {
    display: inline-flex; align-items: center; justify-content: center; gap: 12px;
    width: 176px; height: 38px; background: var(--button); color: var(--white);
    font-size: 16px; font-weight: 700; text-transform: uppercase; letter-spacing: .3px;
    text-decoration: none;
  }
  .cta svg { width: 10px; height: 12px; }

  /* Footer */
  .footer {
    position: absolute; left: 0; top: 1068px; width: 776px; height: 132px;
    background: var(--footer-bg); text-align: center; color: var(--grey-text);
    font-size: 14px; line-height: 1.5; padding: 22px 90px 0;
  }
  .footer a { color: var(--ink); font-weight: 700; }
  .footer .copyright { margin-top: 14px; font-size: 13px; }
</style>
</head>
<body>
<div class="email">
  <header class="hero">
    <div class="hero-photo" role="img" aria-label="Smiling student holding a pen, books under her arm"></div>
    <svg class="hero-swoosh" viewBox="0 0 776 372" aria-hidden="true">
      <path d="M0 318 C 220 372, 520 352, 776 248 L776 372 L0 372 Z" fill="#ffffff"/>
      <path d="M0 300 C 230 360, 520 340, 776 232 L776 250 C 520 356, 230 378, 0 322 Z" fill="#a9c83b"/>
    </svg>
    <div class="brand">CampusLedger.org</div>
    <h1 class="hero-title">Degrees from accredited college and universities</h1>
  </header>

  <nav class="tiles">
    <div class="tile">
      <div class="tile-photo subject" role="img" aria-label="Student studying at a desk"></div>
      <div class="tile-label">Degree by subject</div>
    </div>
    <div class="tile">
      <div class="tile-photo level" role="img" aria-label="Graduates in caps and gowns"></div>
      <div class="tile-label">Degree by level</div>
    </div>
    <div class="tile">
      <div class="tile-photo state" role="img" aria-label="University campus building"></div>
      <div class="tile-label">School by state</div>
    </div>
    <div class="tile">
      <div class="tile-photo online" role="img" aria-label="Person studying online on a laptop"></div>
      <div class="tile-label">Online school</div>
    </div>
  </nav>

  <table class="salary-table">
    <colgroup><col class="occupation"><col class="salary"><col class="action"></colgroup>
    <thead>
      <tr><th>Occupation type</th><th>Median salary</th><th>Next step</th></tr>
    </thead>
    <tbody>
      <tr>
        <td class="occupation-cell">Preschool and Childcare<br>Center/Program</td>
        <td class="salary-cell"><strong>$51,290</strong> per year</td>
        <td class="action-cell"><a class="cta" href="#">Get started <svg viewBox="0 0 10 12"><path d="M0 0 L10 6 L0 12 Z" fill="#fff"/></svg></a></td>
      </tr>
      <tr>
        <td class="occupation-cell">Preschool and Childcare<br>Center/Program</td>
        <td class="salary-cell"><strong>$51,290</strong> per year</td>
        <td class="action-cell"><a class="cta" href="#">Get started <svg viewBox="0 0 10 12"><path d="M0 0 L10 6 L0 12 Z" fill="#fff"/></svg></a></td>
      </tr>
      <tr>
        <td class="occupation-cell">Preschool and Childcare<br>Center/Program</td>
        <td class="salary-cell"><strong>$51,290</strong> per year</td>
        <td class="action-cell"><a class="cta" href="#">Get started <svg viewBox="0 0 10 12"><path d="M0 0 L10 6 L0 12 Z" fill="#fff"/></svg></a></td>
      </tr>
      <tr>
        <td class="occupation-cell">Preschool and Childcare<br>Center/Program</td>
        <td class="salary-cell"><strong>$51,290</strong> per year</td>
        <td class="action-cell"><a class="cta" href="#">Get started <svg viewBox="0 0 10 12"><path d="M0 0 L10 6 L0 12 Z" fill="#fff"/></svg></a></td>
      </tr>
      <tr>
        <td class="occupation-cell">Preschool and Childcare<br>Center/Program</td>
        <td class="salary-cell"><strong>$51,290</strong> per year</td>
        <td class="action-cell"><a class="cta" href="#">Get started <svg viewBox="0 0 10 12"><path d="M0 0 L10 6 L0 12 Z" fill="#fff"/></svg></a></td>
      </tr>
    </tbody>
  </table>

  <footer class="footer">
    <p>We hope you enjoyed receiving this email. Should you no longer wish to receive emails from this company visit this link to <a href="#">unsubscribe</a>.</p>
    <p class="copyright">Copyright © CampusLedger.org &nbsp;|&nbsp; All Rights Reserved.</p>
  </footer>
</div>
</body>
</html>
```